Law firm website marketed direct to many individual clients

I need someone to design a very basic website for a law firm that will be very eye catching. It's going to be a single-paged, scrolling website with a small number of folds. I have uploaded a simple word document that outlines the basics of what I thought could be the layout, but I am open to suggestion on font, size, shades of color, organization, etc. etc. Essentially the website just needs to be a very efficient and visually appealing way of conveying some simple messages.

Target Market(s)

High volumes of individuals who have gotten into a car accident and then google on their phones a lawyer to hire to represent them.

Industry/Entity Type

Legal

Number of Pages Required

1 page

Font styles to use
Serif
Sans Serif

Colors
34a7d7
85cae6
0592cd

Requirements
Must have
• Must be bright and grab the users attention with color scheme and layout. The different sections should be done in such a way that they can fit entirely onto one smart phone or tablet screen.
Nice to have
• I'd like to try and see what it looks like if in the middle somewhere there is a fold that says "MEET YOUR ATTORNEYS" and includes individual photos of two attorneys, one on the left side and one on the right. And then a small bio section on them. I don't want the photos to include a square or rectangle background, I want the person in the photo to be superimposed on top of whatever pattern or background you have in the fold.
Should not have
• Do not want too much text. Anything more than 2 sentences in any single place is unacceptable.

```html
<!DOCTYPE html>
<html lang="en">
<head>
<meta charset="utf-8">
<title>Harborline Law Group</title>
<link href="https://fonts.googleapis.com/css2?family=Cinzel:wght@400;600;700&family=Lato:wght@400;700&display=swap" rel="stylesheet">
<style>
:root{
  --blue:#34a7d7;
  --blue-light:#85cae6;
  --blue-deep:#0592cd;
  --ink:#1b1b1b;
  --grey-band:#ececec;
  --footer-dark:#333333;
  --white:#ffffff;
}
*{margin:0;padding:0;box-sizing:border-box}
html,body{width:914px;height:1200px;overflow:hidden;background:var(--white)}
body{position:relative;font-family:'Lato',sans-serif;color:var(--ink)}
.serif{font-family:'Cinzel',serif}

.site-header{position:absolute;top:0;left:0;width:914px;height:81px;border-top:3px solid #111;background:var(--white)}
.brand{position:absolute;left:52px;top:18px;display:flex;align-items:center;gap:10px}
.brand-mark{width:22px;height:22px;background:var(--blue-deep)}
.brand-name{font-family:'Cinzel',serif;font-weight:600;font-size:19px;line-height:21px;color:#1b1b1b}
.header-call{position:absolute;right:52px;top:16px;display:flex;align-items:center;gap:6px}
.header-call .label{font-size:15px;font-weight:700;color:#333;line-height:19px}
.header-call .number{font-size:15px;color:#333;line-height:19px}

.hero{position:absolute;top:81px;left:0;width:914px;height:347px;background:linear-gradient(100deg,#2f93c2 0%,#34a7d7 45%,#4cb3de 70%,#2e9fd2 100%);color:var(--white);text-align:center}
.hero-title{position:absolute;width:100%;font-family:'Cinzel',serif;font-weight:600}
.hero-title.t1{top:56px;font-size:23px}
.hero-title.t2{top:105px;font-size:24px}
.hero-title.t3{top:137px;font-size:31px}
.hero-call{position:absolute;left:357px;top:202px;width:200px;height:40px;border:1px solid rgba(255,255,255,.8);border-radius:3px;background:var(--blue-light);display:flex;align-items:center;overflow:hidden}
.hero-call .icon-cap{width:40px;height:100%;background:var(--blue);border-radius:0 20px 20px 0;display:flex;align-items:center;justify-content:center}
.hero-call .num{flex:1;font-size:19px;font-weight:700;color:#1b1b1b;padding-right:8px}
.learn-more{position:absolute;top:292px;width:100%;font-size:14px;font-weight:700;letter-spacing:.2px}
.learn-more svg{display:block;margin:4px auto 0}

.feature{position:absolute;left:0;width:914px;text-align:center}
.feature-head{display:flex;align-items:center;justify-content:center;gap:8px}
.feature-icon{width:30px;height:30px;border-radius:50%;background:var(--blue-light);display:flex;align-items:center;justify-content:center}
.feature-title{font-family:'Cinzel',serif;font-weight:600;font-size:24px;color:var(--blue-deep);line-height:30px}
.feature-text{font-size:13px;margin-top:4px;line-height:18px}

.call-btn{position:absolute;left:366px;width:182px;height:37px;background:var(--blue-deep);border-radius:2px;display:flex;align-items:center;overflow:hidden;color:var(--white)}
.call-btn .icon-cap{width:37px;height:100%;background:var(--blue-light);border-radius:0 18px 18px 0;display:flex;align-items:center;justify-content:center}
.call-btn .num{flex:1;text-align:center;font-size:18px;font-weight:700;padding-right:6px}

.trust-band{position:absolute;top:808px;left:0;width:914px;height:274px;background:linear-gradient(160deg,#e4e4e4 0%,#f5f5f5 40%,#e8e8e8 70%,#f2f2f2 100%)}

.site-footer{position:absolute;top:1082px;left:0;width:914px;height:80px;background:var(--blue-deep);color:var(--white)}
.footer-item{position:absolute;top:24px;display:flex;align-items:center;gap:13px;font-size:11.5px;line-height:14px}
.footer-icon{width:31px;height:31px;background:rgba(255,255,255,.35);border-radius:2px;display:flex;align-items:center;justify-content:center}
.copyright{position:absolute;top:1162px;left:0;width:914px;height:38px;background:var(--footer-dark);color:#eee;font-size:10.5px;text-align:center;line-height:38px}
</style>
</head>
<body>

<header class="site-header">
  <div class="brand">
    <span class="brand-mark"></span>
    <span class="brand-name">Harborline<br>Law Group</span>
  </div>
  <div class="header-call">
    <svg width="40" height="48" viewBox="0 0 40 48"><circle cx="22" cy="24" r="17" fill="none" stroke="#0592cd" stroke-width="2"/><path d="M13 15c3-2 5 4 3 6-1 1 1 6 5 9 2 1 5-1 6 2s-4 5-6 4c-5-2-11-10-11-16 0-2 1-4 3-5z" fill="#0592cd"/></svg>
    <div><div class="label">Call Us:</div><div class="number">504-555-0182</div></div>
  </div>
</header>

<section class="hero" role="img" aria-label="Photo of an injured man sitting beside a crashed car, tinted blue">
  <div class="hero-title t1">Accident? Injured?</div>
  <div class="hero-title t2">Your Case</div>
  <div class="hero-title t3">Your Money</div>
  <div class="hero-call">
    <span class="icon-cap"><svg width="20" height="20" viewBox="0 0 24 24"><path d="M6.6 10.8a15 15 0 0 0 6.6 6.6l2.2-2.2c.3-.3.7-.4 1-.2 1.1.4 2.3.6 3.6.6.6 0 1 .4 1 1V20c0 .6-.4 1-1 1A17 17 0 0 1 3 4c0-.6.4-1 1-1h3.5c.6 0 1 .4 1 1 0 1.3.2 2.5.6 3.6.1.3 0 .7-.2 1z" fill="#111"/></svg></span>
    <span class="num">504-555-0182</span>
  </div>
  <div class="learn-more">LEARN MORE
    <svg width="16" height="14" viewBox="0 0 16 14"><path d="M2 2l6 5 6-5M2 7l6 5 6-5" fill="none" stroke="#fff" stroke-width="1.5"/></svg>
  </div>
</section>

<section class="feature" style="top:447px">
  <div class="feature-head"><span class="feature-icon"><svg width="16" height="16" viewBox="0 0 16 16"><rect x="3" y="4" width="10" height="9" rx="1" fill="#fff"/></svg></span><h2 class="feature-title">Low Fees</h2></div>
  <p class="feature-text">We charge less, so you keep more</p>
</section>
<section class="feature" style="top:520px">
  <div class="feature-head"><span class="feature-icon"><svg width="16" height="16" viewBox="0 0 16 16"><circle cx="5" cy="5" r="2" fill="#fff"/><circle cx="11" cy="5" r="2" fill="#fff"/><rect x="2" y="9" width="12" height="3" fill="#fff"/></svg></span><h2 class="feature-title">Free Consultation</h2></div>
  <p class="feature-text">It's always free to talk to us</p>
</section>
<section class="feature" style="top:593px">
  <div class="feature-head"><span class="feature-icon"><svg width="16" height="16" viewBox="0 0 16 16"><rect x="5" y="2" width="7" height="12" rx="1" fill="#fff"/></svg></span><h2 class="feature-title">Get Started Using Only Your Phone</h2></div>
  <p class="feature-text">No need to come to the office, sign up using your phone</p>
</section>
<section class="feature" style="top:666px">
  <div class="feature-head"><span class="feature-icon"><svg width="16" height="16" viewBox="0 0 16 16"><path d="M2 6h3l4-3v10l-4-3H2z" fill="#fff"/><path d="M11 5q2 3 0 6M13 3q4 5 0 10" stroke="#fff" fill="none"/></svg></span><h2 class="feature-title">Speak Directly To A Lawyer</h2></div>
  <p class="feature-text">No staff screening. Talk right to a lawyer on your first call</p>
</section>

<a class="call-btn" style="top:748px">
  <span class="icon-cap"><svg width="18" height="18" viewBox="0 0 24 24"><path d="M6.6 10.8a15 15 0 0 0 6.6 6.6l2.2-2.2c.3-.3.7-.4 1-.2 1.1.4 2.3.6 3.6.6.6 0 1 .4 1 1V20c0 .6-.4 1-1 1A17 17 0 0 1 3 4c0-.6.4-1 1-1h3.5c.6 0 1 .4 1 1 0 1.3.2 2.5.6 3.6.1.3 0 .7-.2 1z" fill="#fff"/></svg></span>
  <span class="num">504-555-0182</span>
</a>

<section class="trust-band"></section>
<section class="feature" style="top:843px">
  <div class="feature-head"><span class="feature-icon"><svg width="18" height="18" viewBox="0 0 18 18"><circle cx="9" cy="9" r="6" fill="none" stroke="#fff" stroke-width="1.5"/><path d="M4 4l10 10" stroke="#fff" stroke-width="1.5"/></svg></span><h2 class="feature-title">No Fee Unless We Win</h2></div>
  <p class="feature-text">We don't get paid unless you get paid. It's as simple as that. We let our results do the talking for us</p>
</section>
<section class="feature" style="top:917px">
  <div class="feature-head"><span class="feature-icon"><svg width="16" height="16" viewBox="0 0 16 16"><text x="8" y="13" text-anchor="middle" font-family="Lato,sans-serif" font-weight="700" font-size="14" fill="#fff">?</text></svg></span><h2 class="feature-title">Questions About Anything?</h2></div>
  <p class="feature-text">We're here to help. Feel free to call us at 504-555-0182 to speak to one of our attorneys. With extensive<br>experience in helping clients get the results that they want, our team is always just a phone call away</p>
</section>

<a class="call-btn" style="top:1010px">
  <span class="icon-cap"><svg width="18" height="18" viewBox="0 0 24 24"><path d="M6.6 10.8a15 15 0 0 0 6.6 6.6l2.2-2.2c.3-.3.7-.4 1-.2 1.1.4 2.3.6 3.6.6.6 0 1 .4 1 1V20c0 .6-.4 1-1 1A17 17 0 0 1 3 4c0-.6.4-1 1-1h3.5c.6 0 1 .4 1 1 0 1.3.2 2.5.6 3.6.1.3 0 .7-.2 1z" fill="#fff"/></svg></span>
  <span class="num">504-555-0182</span>
</a>

<footer class="site-footer">
  <div class="footer-item" style="left:240px">
    <span class="footer-icon"><svg width="14" height="18" viewBox="0 0 14 18"><path d="M7 1a6 6 0 0 1 6 6c0 4-6 10-6 10S1 11 1 7a6 6 0 0 1 6-6z" fill="#fff"/><circle cx="7" cy="7" r="2" fill="#5fb6dd"/></svg></span>
    <span>Harborline Law Group Main Office, Canal Street<br>New Orleans, LA 70112</span>
  </div>
  <div class="footer-item" style="left:557px">
    <span class="footer-icon"><svg width="16" height="16" viewBox="0 0 24 24"><path d="M6.6 10.8a15 15 0 0 0 6.6 6.6l2.2-2.2c.3-.3.7-.4 1-.2 1.1.4 2.3.6 3.6.6.6 0 1 .4 1 1V20c0 .6-.4 1-1 1A17 17 0 0 1 3 4c0-.6.4-1 1-1h3.5c.6 0 1 .4 1 1 0 1.3.2 2.5.6 3.6.1.3 0 .7-.2 1z" fill="#fff"/></svg></span>
    <span>Call Us<br>504-555-0182</span>
  </div>
</footer>
<div class="copyright">Copyright © 2016 Harborline Law Group. All Rights Reserved.</div>

</body>
</html>
```